Online-Marketing Material für Autorin, Ghostwriterin, Buchmentorin
Thank you so much, Glimmerfox, for the great work you did for me. I recommend working with you to everybody who wishes to have very well crafted, efficient marketing materials that exactly meet your CI in style and emotion. All very best :)
Zielgruppe
Ich bin Autorin, Ghostwriterin, Buchmentorin und helfe Unternehmern und Selbständigen auf dem Weg zum eigenen Buch. Meine Zielgruppe sind Menschen, die ein eigenes Unternehmen haben und durch ein Expertenbuch ihren Expertenstatus steigern wollen. Hauptzielgruppe sind z. B. Speaker, Trainer, Coaches, Berater.
Aufgabenstellung
Dieses Design dient dem Online-Marketing für meine neue Online-Akademie (Online Kurse und Masterclasses).
Die Kurse dienen den Kunden dazu, von der ersten Idee bis zum fertigen Buch alles Wissenswerte und Essenzielle über das professionelle, leichte und erfolgreiche Bücherschreiben, Publizieren und die Buchvermarktung zu erfahren.
Ich möchte, dass das Design eine gewisse 'Größe' ausstrahlt, sodass sich Unternehmer:innen angezogen fühlen, die bereit sind, in sich und die Zusammenarbeit mit mir zu investieren. Gleichzeitig soll das Design Leichtigkeit und Machbarkeit des Buchschreibprozesses und der Umsetzung mit mir ausstrahlen. Meine Firmenfarben sind Türkis und Sonnengelb.
Ich bin unentschlossen, ob ein Foto von mir mit aufgegriffen werden sollte. Ich lade mal eins mit hoch :)

```html
<!DOCTYPE html>
<html lang="de">
<head>
<meta charset="utf-8">
<title>Linda Marie Koss – Cover Banner</title>
<link href="https://fonts.googleapis.com/css2?family=Kanit:ital,wght@1,400;1,500;1,600&display=swap" rel="stylesheet">
<style>
  :root {
    --page-bg: #ffffff;
    --turquoise: #3bb8e3;
    --turquoise-deep: #1f9fd0;
    --sun-yellow: #f6c21c;
    --white: #ffffff;
  }
  * { margin: 0; padding: 0; box-sizing: border-box; }
  html, body {
    width: 1200px;
    height: 938px;
    overflow: hidden;
    background: var(--page-bg);
    font-family: "Kanit", sans-serif;
  }
  .cover-banner {
    position: absolute;
    left: 0;
    top: 247px;
    width: 1200px;
    height: 443px;
    overflow: hidden;
  }
  .cover-art { position: absolute; inset: 0; }
  .headline {
    position: absolute;
    left: 763px;
    transform: translateX(-50%);
    color: var(--white);
    font-style: italic;
    white-space: nowrap;
    line-height: 1;
  }
  .headline--intro { top: 74px; font-size: 45px; font-weight: 500; }
  .headline--key { top: 116px; font-size: 68px; font-weight: 600; letter-spacing: 0.5px; }
  .headline--outro { top: 192px; font-size: 45px; font-weight: 500; }
  .cta-button {
    position: absolute;
    left: 622px;
    top: 261px;
    width: 331px;
    height: 48px;
    border-radius: 24px;
    background: var(--sun-yellow);
    color: var(--white);
    font-style: italic;
    font-weight: 500;
    font-size: 32px;
    display: flex;
    align-items: center;
    justify-content: center;
    gap: 14px;
  }
  .cta-button svg { width: 18px; height: 22px; }
  .brand-name {
    position: absolute;
    left: 600px;
    top: 386px;
    display: flex;
    align-items: center;
    gap: 16px;
    color: var(--turquoise-deep);
    font-style: italic;
    font-weight: 500;
    font-size: 34px;
    white-space: nowrap;
  }
  .brand-sun {
    width: 24px;
    height: 24px;
    border-radius: 50%;
    background: var(--sun-yellow);
  }
</style>
</head>
<body>
  <section class="cover-banner">
    <svg class="cover-art" viewBox="0 0 1200 443" width="1200" height="443">
      <defs>
        <linearGradient id="backdropTone" x1="0" y1="0" x2="1" y2="1">
          <stop offset="0" stop-color="#4cc0e8"/>
          <stop offset="0.5" stop-color="#3bb8e3"/>
          <stop offset="1" stop-color="#2eaedd"/>
        </linearGradient>
        <linearGradient id="portraitTone" x1="0" y1="0" x2="0" y2="1">
          <stop offset="0" stop-color="#9fc3d4"/>
          <stop offset="0.4" stop-color="#5b8aa6"/>
          <stop offset="1" stop-color="#2f5f7e"/>
        </linearGradient>
      </defs>
      <rect role="img" aria-label="Hintergrundfoto: Hand mit Stift beim Schreiben, in Türkis getönt" x="0" y="0" width="1200" height="443" fill="url(#backdropTone)"/>
      <path role="img" aria-label="Foto eines lächelnden Mannes mit Brille im blauen Pullover, sitzend" d="M64 443 L90 250 Q110 165 180 140 L190 35 Q250 12 310 40 L318 160 Q370 260 420 330 L500 443 Z" fill="url(#portraitTone)" opacity="0.9"/>
      <path class="wave" d="M470 443 C 640 400, 860 372, 1200 398 L1200 443 Z" fill="var(--white)"/>
    </svg>

    <p class="headline headline--intro">Verbessern Sie Ihren</p>
    <p class="headline headline--key">Expertenstatus</p>
    <p class="headline headline--outro">durch das Schreiben eines Buches</p>

    <div class="cta-button">
      <span>Jetzt anmelden</span>
      <svg viewBox="0 0 18 22"><path d="M0 0 L18 11 L0 22 Z" fill="var(--white)"/></svg>
    </div>

    <div class="brand-name">
      <span>Linda Marie Koss</span>
      <span class="brand-sun"></span>
    </div>
  </section>
</body>
</html>
```